Home & Landing Page REDESIGN needed for Psychology Group

We need a redesign for the template home and landing pages for our psychology group.

Ideally we want a similar layout in the core features, but we want a newer, fresher and more professional design overall.

Our developer will implement the changes from the winning design.

Logo to stay the same.

Please ensure you stay within the same color scheme as the LOGOs 3 main colors.

We want to convey professional, modern, friendly and caring.

Here is the main page template:

http://www.lowrenclinic.com.au/psychologist-melbourne/

and

http://www.lowrenclinic.com.au

*note: we are creating an intro video, please ensure it is included in your brief, near the top of the site* - it is not included on the current site yet but we need it included in all designs.

Target Market(s)

people suffering anxiety, depression or stress that need a psychologist

Industry/Entity Type

Psychology

Number of Pages Required

2 page

Font styles to use
Sans Serif

Colors
86cfc6
85cae6
b7a5cd

Requirements
Must have
• search bar functionality in the top fold of the page, strong focus that we are experienced in anxiety, depression and stress counselling.
• Lots of images and pictures.
• **MUST HAVE: the search square area as it is, unfortunately this cannot be a bar due to development issues with the theme. Please make sure all designs have the search function like it is showing (in a square/rectangle)**
• Must also keep:
• - content area for both home page and city landing pages
• - banner area with search bar same style
• - an area for faqs and blog
• - locations across Australia
• We want most of the same areas, just a refresh so they look better and more polished and professional.
• We are also having an intro video designed, so please include that in your design. (its not in our current web design, but needs to be in the new design)
Should not have
• No orange type colors

```html
<!DOCTYPE html>
<html lang="en">
<head>
<meta charset="utf-8">
<title>Lowren Clinic – Anxiety &amp; Depression Psychologists</title>
<link href="https://fonts.googleapis.com/css2?family=Open+Sans:wght@300;400;600&display=swap" rel="stylesheet">
<style>
  :root{
    --purple:#8a62c8;
    --purple-dark:#6f47b0;
    --mint:#56d6ae;
    --teal:#86cfc6;
    --sky:#85cae6;
    --lavender:#b7a5cd;
    --grey-bg:#ededed;
    --grey-line:#d6d6d6;
    --text:#555a5e;
    --text-light:#8a8f93;
    --white:#ffffff;
  }
  *{box-sizing:border-box;margin:0;padding:0}
  html,body{width:1200px;height:2443px;overflow:hidden;background:var(--white)}
  body{font-family:"Open Sans",Arial,sans-serif;color:var(--text);position:relative}
  .abs{position:absolute}

  /* top bar */
  .util-links{left:36px;top:8px;font-size:13px;display:flex;gap:18px;color:var(--purple)}
  .consult-link{left:715px;top:31px;font-size:10px;color:var(--mint);letter-spacing:.3px;white-space:nowrap}
  .btn-appointment{left:900px;top:24px;width:156px;height:30px;background:var(--purple);color:var(--white);font-size:12px;font-weight:600;display:flex;align-items:center;justify-content:center;letter-spacing:.3px}
  .brand{left:90px;top:64px;display:flex;align-items:center;gap:14px}
  .brand-dot{width:58px;height:58px;border-radius:50%;background:var(--teal)}
  .brand-name{font-size:38px;font-weight:400;color:var(--purple);letter-spacing:.5px}
  .brand-tag{left:92px;top:128px;font-size:11px;letter-spacing:2px;color:var(--text-light)}

  /* nav */
  .main-nav{left:0;top:147px;width:1200px;height:42px;background:var(--mint);display:flex;align-items:center;padding-left:90px;gap:22px;color:var(--white);font-size:15px;letter-spacing:.4px}

  /* hero */
  .hero-photo{left:0;top:189px;width:1200px;height:681px;background:radial-gradient(ellipse at 55% 45%,#f3c7c2 0%,#c99a86 30%,#6e5b4e 65%,#3a3430 100%)}
  .hero-title-band{left:0;top:232px;width:1200px;height:52px;background:rgba(255,255,255,.35)}
  .hero-title{left:0;top:238px;width:1200px;text-align:center;font-size:31px;font-weight:300;color:var(--purple);letter-spacing:.5px}
  .hero-foot{left:0;top:870px;width:1200px;height:18px;background:#dcdcdc}

  .search-box{left:30px;top:549px;width:255px;height:285px;background:rgba(120,90,180,.55);border:5px solid var(--purple);padding:22px 18px;color:var(--white);font-size:12px}
  .search-label{letter-spacing:.5px;margin-bottom:6px}
  .search-select{height:24px;background:rgba(255,255,255,.85);display:flex;justify-content:space-between;align-items:center;padding-left:8px;color:var(--text-light);font-size:11px;margin-bottom:18px}
  .search-select span.arrow{width:24px;height:24px;background:var(--purple);display:flex;align-items:center;justify-content:center}
  .search-range{height:8px;background:rgba(255,255,255,.5);margin:10px 0 6px;position:relative}
  .search-range::before{content:"";position:absolute;left:0;top:0;width:55%;height:8px;background:var(--purple)}
  .search-submit{position:absolute;right:18px;bottom:16px;width:62px;height:22px;background:var(--purple);font-size:11px;display:flex;align-items:center;justify-content:center}

  /* services */
  .services{left:0;top:888px;width:1200px;height:756px;background:var(--grey-bg)}
  .service-photo{height:186px}
  .icon-ring{width:138px;height:138px;border-radius:50%;background:var(--white);display:flex;align-items:center;justify-content:center;box-shadow:0 2px 6px rgba(0,0,0,.15)}
  .icon-ring .core{width:112px;height:112px;border-radius:50%;display:flex;align-items:center;justify-content:center}
  .core.purple{background:var(--purple)}
  .core.mint{background:var(--mint)}
  .service-title{font-size:22px;font-weight:400;letter-spacing:.5px;width:540px;text-align:center}
  .service-title.purple{color:var(--purple)}
  .service-title.mint{color:var(--mint)}
  .service-text{font-size:15px;line-height:19px;color:var(--text);width:560px}
  .service-text.right{text-align:right}

  /* faq + video */
  .feature-band{left:0;top:1644px;width:1200px;height:441px;background:var(--mint)}
  .faq-panel{left:30px;top:1665px;width:570px;height:399px;background:#eefaf6;box-shadow:0 2px 6px rgba(0,0,0,.15);padding:22px 26px}
  .faq-panel h2{font-size:40px;font-weight:400;color:var(--text);margin-bottom:10px}
  .faq-panel p{font-size:15px;line-height:19px;margin-bottom:19px}
  .faq-list{list-style:none;font-size:15px;line-height:19px;margin-top:40px}
  .video-panel{left:624px;top:1665px;width:522px;height:399px;background:linear-gradient(135deg,#7cc7c0 0%,#4f8d88 45%,#c79a7c 75%,#8c6a55 100%);box-shadow:0 2px 6px rgba(0,0,0,.2)}
  .play-btn{left:699px;top:1830px;width:90px;height:90px;border-radius:50%;background:rgba(255,255,255,.9);display:flex;align-items:center;justify-content:center}
  .video-caption{left:760px;top:1970px;font-size:40px;font-weight:300;color:rgba(255,255,255,.8)}
  .feature-foot{left:0;top:2085px;width:1200px;height:30px;background:#e3e3e3}

  /* footer */
  .foot-heading{font-size:19px;font-weight:400;color:var(--purple);letter-spacing:.5px;white-space:nowrap}
  .cat-list{left:36px;top:2218px;list-style:none;font-size:11px;line-height:15px;color:var(--text-light)}
  .foot-divider{left:264px;top:2178px;width:2px;height:150px;background:var(--purple)}
  .join-text{left:300px;top:2222px;width:350px;text-align:center;font-size:11px;line-height:16px;color:var(--text-light)}
  .contact-row{display:flex;align-items:center;gap:10px;font-size:14px;color:var(--text);white-space:nowrap}
  .site-search-label{left:684px;top:2252px;font-size:12px;color:var(--purple);letter-spacing:.4px}
  .site-search-input{left:684px;top:2268px;width:126px;height:18px;background:var(--mint);font-size:10px;color:var(--white);padding-left:6px;line-height:18px}
  .map-area{left:950px;top:2140px;width:232px;height:205px;background:linear-gradient(160deg,#f1f1f1,#e2e2e2);border-radius:40px 60px 30px 80px}
  .copyright-bar{left:0;top:2355px;width:1200px;height:88px;background:var(--mint);display:flex;align-items:center;justify-content:center;color:var(--white);font-size:11px}
</style>
</head>
<body>

<header>
  <nav class="abs util-links"><span>About Us</span><span>Therapist We Use</span><span>Join Our Associate Program</span><span>Blog</span></nav>
  <div class="abs consult-link">BOOK A FREE CONSULTATION</div>
  <div class="abs btn-appointment">MAKE AN APPOINTMENT</div>
  <div class="abs brand"><span class="brand-dot"></span><span class="brand-name">Lowren Clinic</span></div>
  <div class="abs brand-tag">HELPING YOU CREATE A LIFE YOU LOVE</div>
  <nav class="abs main-nav"><span>HOME</span><span>COUNSELLING TYPES ˅</span><span>PSYCHOLOGIST LOCATIONS ˅</span><span>FAQS</span><span>FEES &amp; REBATES</span><span>QUIZZES ˅</span><span>CONTACT</span></nav>
</header>

<section class="hero">
  <div class="abs hero-photo" role="img" aria-label="Smiling young girl in a pink hat sitting outdoors"></div>
  <div class="abs hero-title-band"></div>
  <h1 class="abs hero-title">EXPERIENCED AND CARING ANXIETY &amp; DEPRESSION PSYCHOLOGISTS</h1>
  <form class="abs search-box">
    <div class="search-label">SEARCH FOR:</div>
    <div class="search-select">Select therapy type<span class="arrow"><svg width="10" height="6" viewBox="0 0 10 6"><path d="M0 0h10L5 6z" fill="#fff"/></svg></span></div>
    <div class="search-label">SEARCH NEAR:</div>
    <div class="search-select">Suburb<span class="arrow"><svg width="10" height="6" viewBox="0 0 10 6"><path d="M0 0h10L5 6z" fill="#fff"/></svg></span></div>
    <div class="search-select">Select your state<span class="arrow"><svg width="10" height="6" viewBox="0 0 10 6"><path d="M0 0h10L5 6z" fill="#fff"/></svg></span></div>
    <div style="font-size:10px">Search in radius 20 kilometres</div>
    <div class="search-range"></div>
    <div class="search-submit">SUBMIT</div>
  </form>
  <div class="abs hero-foot"></div>
</section>

<section class="abs services"></section>
<!-- depression -->
<div class="abs service-photo" style="left:135px;top:900px;width:510px;background:linear-gradient(90deg,#d9cfc8,#8a6f62 60%,#3b302c)" role="img" aria-label="Woman resting her head in her hand looking sad"></div>
<div class="abs icon-ring" style="left:30px;top:930px"><div class="core purple">
  <svg width="60" height="50" viewBox="0 0 60 50"><path d="M14 38a12 12 0 0 1 2-24 16 16 0 0 1 30 2 11 11 0 0 1 0 22z" fill="none" stroke="#fff" stroke-width="4"/></svg>
</div></div>
<h3 class="abs service-title purple" style="left:30px;top:1100px">DEPRESSION</h3>
<p class="abs service-text" style="left:36px;top:1155px">Are you feeling empty, hopeless and despairing?<br>Do you have huge ups and downs?<br>Or do you have Male depression<br>(discontented with yourself, antagonistic, exaggerated behaviour &amp; avoidance)<br>or post baby blues?</p>

<!-- guarantee -->
<div class="abs service-photo" style="left:609px;top:900px;width:540px;background:linear-gradient(90deg,#9aa5ad,#e6d9cf 55%,#b9c3c8)" role="img" aria-label="Smiling couple standing together"></div>
<div class="abs icon-ring" style="left:1008px;top:930px"><div class="core purple">
  <svg width="56" height="44" viewBox="0 0 56 44"><path d="M5 22l15 15L51 6" fill="none" stroke="#fff" stroke-width="8" stroke-linecap="round" stroke-linejoin="round"/></svg>
</div></div>
<h3 class="abs service-title purple" style="left:630px;top:1100px">GREAT MATCH GUARANTEE</h3>
<p class="abs service-text right" style="left:595px;top:1155px">Are you feeling empty, hopeless and despairing?<br>Do you have huge ups and downs?<br>Or do you have Male depression<br>(discontented with yourself, antagonistic, exaggerated behaviour &amp; avoidance)<br>or post baby blues?</p>

<!-- anxiety -->
<div class="abs service-photo" style="left:36px;top:1275px;width:540px;height:189px;background:linear-gradient(90deg,#6f8f9c,#e7d6b8 50%,#5f7580)" role="img" aria-label="Worried young woman with blonde hair"></div>
<div class="abs icon-ring" style="left:30px;top:1344px"><div class="core mint">
  <svg width="60" height="40" viewBox="0 0 60 40"><path d="M4 12q9-8 17 0t17 0 18 0M4 28q9-8 17 0t17 0 18 0" fill="none" stroke="#fff" stroke-width="4" stroke-linecap="round"/></svg>
</div></div>
<h3 class="abs service-title mint" style="left:30px;top:1470px">ANXIETY</h3>
<p class="abs service-text" style="left:36px;top:1521px">Are you feeling empty, hopeless and despairing?<br>Do you have huge ups and downs?<br>Or do you have Male depression<br>(discontented with yourself, antagonistic, exaggerated behaviour &amp; avoidance)<br>or post baby blues?</p>

<!-- stress -->
<div class="abs service-photo" style="left:606px;top:1275px;width:549px;height:189px;background:linear-gradient(90deg,#3d3a3a,#b98b70 50%,#5a4a42)" role="img" aria-label="Stressed young man leaning over a desk"></div>
<div class="abs icon-ring" style="left:1005px;top:1344px"><div class="core mint">
  <svg width="40" height="56" viewBox="0 0 40 56"><path d="M24 2L6 32h14l-4 22 18-32H20z" fill="#fff"/></svg>
</div></div>
<h3 class="abs service-title mint" style="left:620px;top:1470px">STRESS</h3>
<p class="abs service-text right" style="left:595px;top:1521px">Are you feeling empty, hopeless and despairing?<br>Do you have huge ups and downs?<br>Or do you have Male depression<br>(discontented with yourself, antagonistic, exaggerated behaviour &amp; avoidance)<br>or post baby blues?</p>

<section class="abs feature-band"></section>
<article class="abs faq-panel">
  <h2>FAQ's</h2>
  <p>Exciting news in Treating Anxiety and Depression<br>This enables us to create wonderful new methodologies for helping you overcome these problems.</p>
  <p>The newer methodologies of Mindfulness and Compassionate Therapy are showing extremely positive results.</p>
  <ul class="faq-list">
    <li>What rebates are available?</li>
    <li>What factor creates the best therapeutic help for you?</li>
    <li>What to Expect on Your First Appointment</li>
    <li>What Treatment Modalities do we use as Psychologists?</li>
  </ul>
</article>
<div class="abs video-panel" role="img" aria-label="Intro video still of a smiling young woman"></div>
<div class="abs play-btn"><svg width="34" height="40" viewBox="0 0 34 40"><path d="M4 2l28 18L4 38z" fill="#6b6f73"/></svg></div>
<div class="abs video-caption">Get Started ?</div>
<div class="abs feature-foot"></div>

<footer>
  <h4 class="abs foot-heading" style="left:36px;top:2178px">CATEGORIES</h4>
  <ul class="abs cat-list">
    <li>Anxiety (8)</li><li>Counselling (7)</li><li>Depression (5)</li><li>Personal growth (4)</li><li>Psychological well-being (10)</li><li>Self esteem (3)</li><li>Stress (2)</li>
  </ul>
  <div class="abs foot-divider"></div>
  <h4 class="abs foot-heading" style="left:345px;top:2178px">ARE YOU A PSYCHOLOGIST?</h4>
  <div class="abs join-text">If You're Interested In Joining Our Associate Program Team<br><br>Click Here For More Details<br><br>COPYRIGHT © LOWREN CLINIC ASSOCIATE<br>Click Here To Log In</div>
  <div class="abs map-area" role="img" aria-label="Map of Australia showing clinic locations"></div>
  <div class="abs contact-row" style="left:790px;top:2156px"><svg width="22" height="30" viewBox="0 0 22 30"><path d="M11 0a11 11 0 0 1 11 11c0 8-11 19-11 19S0 19 0 11A11 11 0 0 1 11 0z" fill="#8a62c8"/><circle cx="11" cy="11" r="4" fill="#fff"/></svg>Australia</div>
  <div class="abs contact-row" style="left:790px;top:2196px"><svg width="22" height="22" viewBox="0 0 22 22"><path d="M5 1l4 5-2 3a12 12 0 0 0 6 6l3-2 5 4-3 4C9 21 1 13 1 4z" fill="#8a62c8"/></svg>1300 555 014</div>
  <div class="abs site-search-label">SEARCH OUR WEBSITE</div>
  <div class="abs site-search-input">Search…</div>
  <div class="abs copyright-bar">© Copyright 2016 Lowren Clinic Pty Ltd. All rights reserved.</div>
</footer>

</body>
</html>
```